We need a flyer where we promote a workshop to our members of the jewish community www.vbq-gemeinde.example . The workshop is calles "command in seven weeks presented by VBQ. We would like to see a flyer with the below text is used and also some pictures (attached). The flyer should come over as cool, fresh, innovative for a younger crowd so called young professionals (age 28-35).
TITLE.
"Command in Seven Weeks.
SUBTITLE.
Your systematic self-coaching roadmap to power and impact—and your future.”
TEXT.
Dr. Marcus L. Brandauer is the CEO Emeritus of Alpine Advisory Partners—he made an exit in 2013. He is the award-winning author of 8 books, including "Momentum-By-Design," "Speak Up or Fade" and "The Cantor and the Chairman.”
For the past 20 years he has taught leadership at Harwick University in New York and at KLB (Lindmoor University) to prepare future CEOs and other leaders in business, government , nonprofits and the military.
Now, in a process exclusively designed for VBQ’s next generation of emerging leaders, Marcus unpacks his leadership secrets in 3 action-packed labs—reduced to the max:
Lab 1. Command in Seven Weeks: The Summit Compass Model®. Self-Assessment. Self-Leadership: “The Lantern.” 5-Year Vision. 100-Day Catalytic Project.
Lab 2. Guiding Through Words. Relationship: Building Trust. Momentum-By-Design. Cockpit.
Lab 3. Debrief and Scale-Up. Sustainability. Action Tools.
Do you want to build your own future and a life you love? Do you want to jump-start that future and life over 100 days while learning a toolbox of leadership skills, networking with like-minded people—and even get some pizza? Then join us.
young professionals age 28-35

```html
<!DOCTYPE html>
<html lang="en">
<head>
<meta charset="utf-8">
<title>Command in Seven Weeks – VBQ Flyer</title>
<link rel="stylesheet" href="https://fonts.googleapis.com/css2?family=Poppins:wght@300;400;500;600;700;800&display=swap">
<style>
  :root{
    --blue:#1a2ea0;
    --blue-dark:#101f7a;
    --ink:#2a2a2a;
    --grey:#5a5a5c;
    --grey-text:#555;
    --page:#e8e8e8;
    --white:#ffffff;
    --hero-top:#0d1233;
    --hero-bottom:#1c2f8f;
  }
  *{margin:0;padding:0;box-sizing:border-box}
  html,body{width:1200px;height:2450px;overflow:hidden}
  body{background:var(--page);font-family:"Poppins",Arial,sans-serif;position:relative}
  .flyer{position:absolute;left:40px;top:433px;width:1120px;height:1584px;background:var(--white);overflow:hidden;box-shadow:0 10px 40px rgba(0,0,0,.18)}
  .hero-photo{position:absolute;left:0;top:30px;width:1120px;height:441px;
    background:linear-gradient(180deg,var(--hero-top) 0%,var(--hero-bottom) 100%)}
  .masthead{position:absolute;left:0;top:0;width:1120px;height:150px}
  .brand{position:absolute;left:370px;top:38px;width:380px;display:flex;align-items:center;gap:16px;color:var(--white)}
  .brand-name{font-weight:800;font-size:72px;line-height:1;letter-spacing:-2px}
  .brand-full{font-weight:400;font-size:19px;line-height:1.2}
  .title-band{position:absolute;left:0;top:471px;width:1120px;height:145px;background:var(--blue)}
  .title-line{position:absolute;left:0;width:1120px;text-align:center;font-weight:800;line-height:1;white-space:nowrap}
  .title-line.top{top:470px;font-size:160px;color:var(--white);letter-spacing:-4px}
  .title-line.bottom{top:628px;font-size:118px;color:var(--ink);letter-spacing:-4px}
  .title-line .accent{color:var(--blue)}
  .subtitle{position:absolute;left:0;top:758px;width:1120px;text-align:center;font-weight:700;font-size:24px;letter-spacing:-.3px;color:var(--ink)}
  .bio{position:absolute;left:244px;top:815px;width:792px;height:241px;background:var(--grey);border-radius:14px;color:var(--white);padding:26px 22px 0 105px;font-size:16.5px;font-weight:300;line-height:1.3}
  .bio p+p{margin-top:18px}
  .bio em{font-weight:600}
  .portrait-ring{position:absolute;left:66px;top:795px;width:278px;height:278px;border-radius:50%;background:var(--white)}
  .portrait{position:absolute;left:76px;top:805px;width:258px;height:258px;border-radius:50%;background:radial-gradient(circle at 50% 40%,#8a8a8c 0,#6a6a6c 55%,#4e4e50 100%)}
  .intro{position:absolute;left:77px;top:1090px;width:970px;font-size:18px;line-height:1.3;color:var(--ink);font-weight:400}
  .labs{position:absolute;left:77px;top:1156px;width:966px;display:flex;gap:20px}
  .lab{flex:1;height:185px;border:1.5px solid var(--blue);border-radius:12px;overflow:hidden;background:var(--white)}
  .lab-head{height:48px;background:linear-gradient(180deg,#2b44c4,var(--blue));color:var(--white);text-align:center;font-weight:600;font-size:24px;line-height:48px;border-radius:10px 10px 0 0}
  .lab-body{padding:14px 22px 0;text-align:center;font-size:16px;font-weight:600;line-height:1.27;color:var(--ink)}
  .question{position:absolute;left:0;top:1362px;width:1120px;text-align:center;font-weight:700;font-size:22px;color:var(--blue)}
  .closing{position:absolute;left:90px;top:1400px;width:940px;text-align:center;font-size:17px;line-height:1.3;color:var(--grey-text);font-weight:300}
  .footer{position:absolute;left:0;top:1495px;width:1120px;height:89px}
  .footer svg.band{position:absolute;left:0;top:0}
  .phone{position:absolute;left:76px;top:20px;display:flex;align-items:center;gap:22px;color:var(--white);font-weight:700;font-size:36px;line-height:48px;white-space:nowrap}
  .contact{position:absolute;top:20px;display:flex;gap:10px;color:var(--white);font-size:16px;font-weight:600;line-height:1.3;white-space:nowrap}
  .contact.address{left:470px}
  .contact.web{left:818px}
</style>
</head>
<body>
  <main class="flyer">
    <div class="hero-photo" role="img" aria-label="Photo of a large conference audience watching a speaker on a lit stage"></div>

    <svg class="masthead" viewBox="0 0 1120 150" aria-hidden="true">
      <path fill="#1a2ea0" d="M0 0H1120V30H830C790 30 790 142 745 142H375C330 142 330 30 290 30H0Z"/>
    </svg>
    <div class="brand">
      <span class="brand-name">VBQ</span>
      <span class="brand-full">Vereinigte<br>Bürgergemeinde<br>Quellental</span>
    </div>

    <div class="title-band"></div>
    <h1>
      <span class="title-line top">COMMAND</span>
      <span class="title-line bottom">IN <span class="accent">SEVEN</span> WEEKS</span>
    </h1>
    <p class="subtitle">Your systematic self-coaching roadmap to power and impact—and your future</p>

    <section class="bio">
      <p>Dr. Marcus L. Brandauer is the CEO Emeritus of Alpine Advisory Partners—he made an exit in 2013. He is the award-winning author of 8 books, including <em>“Momentum-By-Design,” “Speak Up or Fade”</em> and <em>“The Cantor and the Chairman.”</em></p>
      <p>For the past <em>20 years</em> he has taught leadership at Harwick University in New York and at KLB (Lindmoor University) to prepare future CEOs and other leaders in business, government , nonprofits and the military.</p>
    </section>
    <div class="portrait-ring"></div>
    <div class="portrait" role="img" aria-label="Portrait photo of Dr. Marcus L. Brandauer"></div>

    <p class="intro">Now, in a process exclusively designed for VBQ’s next generation of emerging leaders, Marcus unpacks his leadership secrets in 3 action-packed labs—reduced to the max:</p>

    <section class="labs">
      <article class="lab">
        <h2 class="lab-head">Lab 1.</h2>
        <p class="lab-body">Command in Seven Weeks: The Summit Compass Model®. Self-Assessment. Self-Leadership: “The Lantern.” 5-Year Vision. 100-Day Catalytic Project.</p>
      </article>
      <article class="lab">
        <h2 class="lab-head">Lab 2.</h2>
        <p class="lab-body">Guiding Through Words. Relationship: Building Trust. Momentum-By-Design. Cockpit.</p>
      </article>
      <article class="lab">
        <h2 class="lab-head">Lab 3</h2>
        <p class="lab-body">Debrief and Scale-Up. Sustainability. Action Tools.</p>
      </article>
    </section>

    <h3 class="question">Do you want to build your own future and a life you love?</h3>
    <p class="closing">Lorem ipsum dolor sit amet, consectetur adipiscing elit, sed do eiusmod tempor incididunt ut labore et dolore magna aliqua. Quis ipsum suspendisse ultrices gravida. Risus commodo viverra maecenas accumsan lacus vel facilisis.</p>

    <footer class="footer">
      <svg class="band" width="1120" height="89" viewBox="0 0 1120 89" aria-hidden="true">
        <rect width="1120" height="89" fill="#5a5a5c"/>
        <path fill="#1a2ea0" d="M0 0H410C440 0 450 30 458 55C464 75 470 89 480 89H0Z"/>
      </svg>
      <div class="phone">
        <svg width="34" height="34" viewBox="0 0 24 24" aria-hidden="true"><path fill="#fff" d="M6.6 10.8a15.1 15.1 0 006.6 6.6l2.2-2.2a1 1 0 011-.25 11.4 11.4 0 003.6.57 1 1 0 011 1V20a1 1 0 01-1 1A17 17 0 013 4a1 1 0 011-1h3.5a1 1 0 011 1c0 1.25.2 2.45.57 3.57a1 1 0 01-.25 1z"/></svg>
        <span>+41 44 555 01 23</span>
      </div>
      <div class="contact address">
        <svg width="26" height="30" viewBox="0 0 24 28" aria-hidden="true"><path fill="none" stroke="#3550d8" stroke-width="2.4" d="M12 2a7 7 0 00-7 7c0 5.2 7 13 7 13s7-7.8 7-13a7 7 0 00-7-7z"/><circle cx="12" cy="9" r="2.6" fill="#3550d8"/><path fill="none" stroke="#3550d8" stroke-width="2" d="M6 24c-2 .6-3 1.2-3 1.8 0 1.2 4 2.2 9 2.2s9-1 9-2.2c0-.6-1-1.2-3-1.8"/></svg>
        <span>VBQ Gemeindezentrum Lindenweg<br>12 8000 Quellental</span>
      </div>
      <div class="contact web">
        <svg width="26" height="26" viewBox="0 0 24 24" aria-hidden="true"><g fill="none" stroke="#3550d8" stroke-width="1.8"><circle cx="12" cy="12" r="10"/><ellipse cx="12" cy="12" rx="4.5" ry="10"/><path d="M2 12h20M4 6.5h16M4 17.5h16"/></g></svg>
        <span>www.vbq-gemeinde.example</span>
      </div>
    </footer>
  </main>
</body>
</html>
```